Sports Nutrition line needs new label look/feel

We need a new label design for "Telmo",our Sports Nutrition line of vitamins, nutraceuticals, protein powders, and performance endurance products. We would like to see two separate designs, one blue and one red, as these are the two colors we are torn between. The labels should have the look/feel of a sports or fitness label, bold coloring, lettering, and even some use of holographic foiling.
Brands we would be similar to those found on pulsevaultshop.com and stridecraftnow.com. Brands we like in particular are QRT and Velmot.

Target Market(s)

Fitness enthusiasts,athletes, health nuts..

Industry/Entity Type

Nutrition

Font styles to use
Sans Serif
Decorative
Script

Colors
ec1f27
0692cd
0355a3
3276b5
f04a50

Requirements
Must have
• -Fitness look/feel
• -bold colors (preferably red and blue)
• -use of icons (eye health, brain, health, etc.)
• -"Fit" in "TelMO" must stand out
• -use tagline "Stronger Every Day"
Nice to have
• -holographic foiling elements
• -try to incorporate a molecular element (like those shown in the example labels)
Should not have
• -Light, calming colors
• -difficult to read fonts

```html
<!DOCTYPE html>
<html lang="en">
<head>
<meta charset="utf-8">
<title>Telmo Grape Seed Extract Label</title>
<link rel="stylesheet" href="https://fonts.googleapis.com/css2?family=Open+Sans:wght@600;700;800&family=Roboto:ital,wght@0,500;0,700;1,700&display=swap">
<style>
  :root {
    --label-red: #b51d2b;
    --label-red-deep: #8f1520;
    --accent-red: #ec1f27;
    --glow-orange: #f26a32;
    --glow-light: #f7a16a;
    --silver: #d9dbe0;
    --silver-dark: #9a9ea6;
    --badge-blue: #0a6fb8;
    --white: #ffffff;
    --page: #ffffff;
  }
  html, body {
    margin: 0;
    width: 1200px;
    height: 1143px;
    overflow: hidden;
    background: var(--page);
  }
  .canvas {
    position: relative;
    width: 1200px;
    height: 1143px;
  }
  .label-art {
    position: absolute;
    left: 0;
    top: 0;
  }
  .brand {
    position: absolute;
    left: 0;
    width: 1200px;
    text-align: center;
    color: var(--white);
  }
  .brand-name {
    top: 395px;
    font: 800 104px/1 "Open Sans", sans-serif;
    letter-spacing: 2px;
  }
  .brand-tagline {
    top: 512px;
    font: 600 17px/1 "Open Sans", sans-serif;
    letter-spacing: 0.5px;
  }
  .product-name {
    position: absolute;
    left: 0;
    width: 1200px;
    text-align: center;
    color: var(--white);
    font-family: "Roboto", sans-serif;
    font-weight: 700;
  }
  .product-line-1 { top: 568px; font-size: 48px; }
  .product-line-2 { top: 624px; font-size: 34px; }
  .claim-ribbon {
    position: absolute;
    left: 370px;
    top: 698px;
    width: 346px;
    text-align: center;
    color: var(--white);
    font: 500 21px/1.3 "Roboto", sans-serif;
  }
  .claim-ribbon strong { font-weight: 700; }
  .supply-badge {
    position: absolute;
    left: 860px;
    top: 708px;
    width: 200px;
    text-align: center;
    color: var(--white);
    font-family: "Roboto", sans-serif;
  }
  .supply-count { font-size: 46px; font-weight: 700; line-height: 1; }
  .supply-days { font-size: 16px; font-weight: 500; margin-top: 6px; }
  .supply-type { font-size: 15px; font-weight: 700; font-style: italic; margin-top: 4px; }
</style>
</head>
<body>
<div class="canvas">
  <svg class="label-art" width="1200" height="1143" viewBox="0 0 1200 1143">
    <defs>
      <linearGradient id="labelBody" x1="0" y1="0" x2="0" y2="1">
        <stop offset="0" stop-color="var(--label-red)"/>
        <stop offset="1" stop-color="var(--label-red-deep)"/>
      </linearGradient>
      <radialGradient id="glowLeft" cx="0" cy="0.5" r="1">
        <stop offset="0" stop-color="var(--glow-light)"/>
        <stop offset="0.55" stop-color="var(--glow-orange)"/>
        <stop offset="1" stop-color="var(--accent-red)"/>
      </radialGradient>
      <radialGradient id="glowRight" cx="1" cy="0.5" r="1">
        <stop offset="0" stop-color="var(--glow-light)"/>
        <stop offset="0.55" stop-color="var(--glow-orange)"/>
        <stop offset="1" stop-color="var(--accent-red)"/>
      </radialGradient>
      <linearGradient id="silverEdge" x1="0" y1="0" x2="0" y2="1">
        <stop offset="0" stop-color="var(--silver-dark)"/>
        <stop offset="0.5" stop-color="var(--silver)"/>
        <stop offset="1" stop-color="var(--silver-dark)"/>
      </linearGradient>
    </defs>

    <rect class="label-body" x="100" y="290" width="1000" height="570" fill="url(#labelBody)"/>

    <path class="side-panel" d="M100 290 H300 Q360 575 300 860 H100 Z" fill="url(#glowLeft)"/>
    <path d="M300 290 Q360 575 300 860" fill="none" stroke="url(#silverEdge)" stroke-width="8"/>
    <path class="side-panel" d="M1100 290 H900 Q840 575 900 860 H1100 Z" fill="url(#glowRight)"/>
    <path d="M900 290 Q840 575 900 860" fill="none" stroke="url(#silverEdge)" stroke-width="8"/>

    <g class="benefit-icons" fill="none" stroke="var(--silver)" stroke-width="3">
      <circle cx="200" cy="420" r="30" role="img" aria-label="Joint health icon"/>
      <circle cx="200" cy="520" r="30" role="img" aria-label="Running leg icon"/>
      <circle cx="200" cy="620" r="30" role="img" aria-label="Muscle strength icon"/>
      <circle cx="1000" cy="420" r="30" role="img" aria-label="Hair health icon"/>
      <circle cx="1000" cy="520" r="30" role="img" aria-label="Brain health icon"/>
      <circle cx="1000" cy="620" r="30" role="img" aria-label="Eye health icon"/>
    </g>

    <path class="ribbon" d="M362 688 H724 L712 758 H350 Z" fill="var(--accent-red)" stroke="var(--silver)" stroke-width="5"/>

    <rect x="100" y="846" width="1000" height="14" fill="var(--accent-red)"/>

    <circle class="badge" cx="960" cy="760" r="95" fill="var(--badge-blue)" stroke="url(#silverEdge)" stroke-width="8"/>
  </svg>

  <div class="brand brand-name">TELMO</div>
  <div class="brand brand-tagline">STRONGER EVERY DAY</div>

  <div class="product-name product-line-1">GRAPE SEED</div>
  <div class="product-name product-line-2">EXTRACT</div>

  <div class="claim-ribbon">ANTIOXIDANT FORMULA<br><strong>TO</strong> BOOST IMMUNITY</div>

  <div class="supply-badge">
    <div class="supply-count">90</div>
    <div class="supply-days">DAY SUPPLY</div>
    <div class="supply-type">DIETARY SUPPLEMENT</div>
  </div>
</div>
</body>
</html>
```